Need Poster Design for Indie Family Film

We need a poster for a indie family film and would like to see designs that should be elegant, bold and playful.

Maribel follows the parallel stories of three Singaporeans dealing with familial love and loss: a young girl copes with her mother’s death by living in an imaginary world, a father struggles to reconcile with his estranged daughter before her wedding and a woman fails to convince her family of her desire to become a singer. Staring Darlene Pruitt, Mirabel Tan with veterans Rosnah Yusof, Farid Osmani and Derek Lam and Calvin Teo

Target Market(s)

7-14 and Parents

Number of Pages Required

3 page

Font styles to use
Serif

Requirements
Must have
• Film Title: Maribel
Nice to have
• The poster doesn't have to incorporate the photos and can use other design elements like illustrations.
Should not have
• Anything offensive and disturbing.

```html
<!DOCTYPE html>
<html lang="en">
<head>
<meta charset="utf-8">
<title>Maribel – Film Poster</title>
<link rel="stylesheet" href="https://fonts.googleapis.com/css2?family=Playfair+Display:wght@900&family=Josefin+Sans:wght@300;600&display=swap">
<style>
  :root {
    --page: #ffffff;
    --frame: #050505;
    --sky-deep: #151c1a;
    --sky-teal: #2f3f39;
    --sky-haze: #bdb8b8;
    --glow-pink: #f0a6ab;
    --glow-red: #e0323f;
    --ground: #000000;
    --title-light: #f6f6f6;
    --title-dark: #8c8c8c;
    --credit: #ffffff;
  }
  * { margin: 0; padding: 0; box-sizing: border-box; }
  html, body {
    width: 1200px;
    height: 900px;
    overflow: hidden;
    background: var(--page);
  }
  .canvas {
    position: relative;
    width: 1200px;
    height: 900px;
    background: var(--page);
  }
  .poster {
    position: absolute;
    left: 283px;
    top: 0;
    width: 636px;
    height: 900px;
    border: 8px solid var(--frame);
    background: var(--frame);
    overflow: hidden;
  }
  .poster__sky {
    position: absolute;
    inset: 0;
    background:
      radial-gradient(ellipse 22% 30% at 97% 64%, rgba(224,50,63,0.9) 0%, rgba(224,50,63,0) 100%),
      radial-gradient(ellipse 38% 26% at 70% 64%, #fbeaea 0%, var(--glow-pink) 45%, rgba(240,166,171,0) 100%),
      radial-gradient(ellipse 35% 18% at 58% 47%, rgba(210,205,205,0.55) 0%, rgba(210,205,205,0) 100%),
      radial-gradient(ellipse 26% 16% at 88% 12%, rgba(205,205,205,0.7) 0%, rgba(205,205,205,0) 100%),
      radial-gradient(ellipse 40% 30% at 85% 30%, rgba(190,185,185,0.6) 0%, rgba(190,185,185,0) 100%),
      radial-gradient(ellipse 18% 14% at 10% 22%, rgba(150,160,155,0.45) 0%, rgba(150,160,155,0) 100%),
      radial-gradient(ellipse 40% 12% at 8% 78%, #c4cbc0 0%, rgba(120,140,125,0.3) 55%, rgba(47,63,57,0) 100%),
      linear-gradient(165deg, var(--sky-deep) 0%, var(--sky-teal) 40%, #575a58 62%, #6c4446 82%, #3a1a1c 100%);
  }
  .poster__ground {
    position: absolute;
    left: 0;
    right: 0;
    top: 712px;
    bottom: 0;
    background:
      linear-gradient(to bottom, rgba(0,0,0,0.55) 0%, #070707 20%, var(--ground) 100%),
      linear-gradient(to right, #2a2a2a 0%, #5a1a1f 100%);
    border-radius: 60% 40% 0 0 / 10px 8px 0 0;
  }
  .poster__title {
    position: absolute;
    top: 106px;
    left: 0;
    right: 0;
    text-align: center;
    font-family: "Playfair Display", "Times New Roman", serif;
    font-weight: 900;
    font-size: 130px;
    line-height: 1;
    letter-spacing: 1px;
    transform: scale(0.78, 1.55);
    transform-origin: 50% 0;
    background: linear-gradient(to bottom, var(--title-light) 10%, #d2d2d2 55%, var(--title-dark) 95%);
    -webkit-background-clip: text;
    background-clip: text;
    color: transparent;
    filter: drop-shadow(3px 4px 3px rgba(0,0,0,0.75));
  }
  .credits {
    position: absolute;
    left: 0;
    right: 0;
    top: 745px;
    text-align: center;
    color: var(--credit);
    font-family: "Josefin Sans", "Helvetica Neue", sans-serif;
    font-size: 9.5px;
    font-weight: 300;
    line-height: 19.2px;
  }
  .credits__line { white-space: nowrap; }
  .credits__role {
    font-weight: 600;
    text-transform: uppercase;
  }
</style>
</head>
<body>
  <main class="canvas">
    <article class="poster">
      <div class="poster__sky" role="img" aria-label="Starry night sky with drifting clouds, glowing pink and red at the right horizon, a lone tree silhouette and two small figures standing on a grassy field"></div>
      <div class="poster__ground"></div>

      <h1 class="poster__title">MARIBEL</h1>

      <footer class="credits">
        <p class="credits__line"><span class="credits__role">Producer:</span> Hollis Brand <span class="credits__role">Co Directors:</span> Idris Mansor and Adele Toh, Hollis Brand</p>
        <p class="credits__line"><span class="credits__role">Cast:</span> Rosnah Yusof, Farid Osmani, Derek Lam, Mirabel Tan, Darlene Pruitt <span class="credits__role">Director of Photography:</span> Elton Ong</p>
        <p class="credits__line"><span class="credits__role">Camera Assistant:</span> Arif Jamal <span class="credits__role">Sound:</span> Sofia Rahim <span class="credits__role">Editor:</span> Jonah Everett Gale</p>
        <p class="credits__line"><span class="credits__role">Production Designer:</span> Joel Chen <span class="credits__role">Production Art Assistant:</span> Amir Nasir &amp; Jared Toh</p>
        <p class="credits__line"><span class="credits__role">Production Assistant:</span> Nadia Omar <span class="credits__role">Assistant Producer:</span> Chen Wei Lin</p>
        <p class="credits__line"><span class="credits__role">Production Company:</span> Lumen Reel Films</p>
      </footer>
    </article>
  </main>
</body>
</html>
```